Velvet Fern Beauty Bar Business Card

We need a modern, elegant business card design for our new beauty bar located in La Quinta, CA. The card should feel premium yet approachable, reflecting our brand identity: warm, stylish, and confidence-boosting.

Use our existing Velvet Fern Beauty Bar logo (to be provided as vector file).

Colors: Black, White, Blush / Nude accents, and Gold (metallic or foil effect if possible).

Typography: Clean sans-serif for clarity, with optional elegant script accent.
Design Style

Minimalist and modern with plenty of white space.

Premium look with a beauty/lifestyle feel (not overly corporate).

Option to explore vertical or horizontal orientation.

Rounded corners welcome, but not required.

Additional Notes

Design should print well in both matte and glossy finishes.

Please present mockups with both light and dark backgrounds.

Keep overall feel sleek, feminine, and high-end while still being approachable.

```html
<!DOCTYPE html>
<html lang="en">
<head>
<meta charset="utf-8">
<title>Velvet Fern Beauty Bar – Business Card</title>
<link rel="stylesheet" href="https://fonts.googleapis.com/css2?family=Lato:ital,wght@0,400;0,700;1,400&family=Marcellus&family=Crimson+Pro:wght@600&display=swap">
<style>
  :root {
    --page: #f8f5f3;
    --blush-light: #f3e1d9;
    --blush: #e4c0b2;
    --nude: #cfa08f;
    --black: #1b1615;
    --gold: #b08d4c;
    --gold-light: #d8bc7f;
    --white: #ffffff;
    --shadow: rgba(40, 25, 20, 0.18);
  }
  * { margin: 0; padding: 0; box-sizing: border-box; }
  html, body { width: 1200px; height: 1200px; overflow: hidden; background: var(--page); }
  .stage { position: relative; width: 1200px; height: 1200px; }

  .card {
    position: absolute;
    left: 256px;
    width: 688px;
    height: 400px;
    border-radius: 28px;
    overflow: hidden;
    color: var(--black);
    box-shadow: 0 8px 22px var(--shadow);
    border: 1px solid var(--gold-light);
  }
  .card--front { top: 180px; }
  .card--back { top: 628px; }

  .card__photo { position: absolute; inset: 0; }
  .card--front .card__photo {
    background:
      radial-gradient(ellipse 55% 60% at 92% 12%, var(--nude) 0%, transparent 72%),
      radial-gradient(ellipse 55% 45% at 28% 45%, var(--white) 0%, transparent 75%),
      linear-gradient(135deg, var(--blush-light) 0%, var(--blush) 100%);
  }
  .card--back .card__photo {
    background:
      radial-gradient(ellipse 40% 35% at 90% 8%, var(--nude) 0%, transparent 75%),
      radial-gradient(ellipse 70% 60% at 50% 55%, var(--white) 0%, transparent 80%),
      linear-gradient(160deg, var(--blush-light) 0%, var(--blush) 100%);
  }

  .lockup { position: absolute; text-align: center; }
  .lockup__tagline {
    font-family: "Lato", sans-serif;
    font-style: italic;
    font-weight: 400;
    color: var(--gold);
  }
  .lockup__name {
    font-family: "Marcellus", serif;
    font-weight: 400;
    line-height: 1;
    letter-spacing: -0.01em;
    white-space: nowrap;
    color: var(--black);
  }
  .lockup__sub {
    font-family: "Lato", sans-serif;
    font-weight: 400;
    display: flex; align-items: center; justify-content: center;
    white-space: nowrap;
  }
  .lockup__sub::before, .lockup__sub::after {
    content: ""; display: block; height: 1.5px; background: var(--gold);
  }

  .card--front .lockup { left: 296px; top: 240px; width: 372px; }
  .card--front .lockup__tagline { font-size: 17px; text-align: left; padding-left: 18px; }
  .card--front .lockup__name { font-size: 54px; margin-top: 2px; }
  .card--front .lockup__sub { font-size: 20px; margin-top: 4px; gap: 10px; }
  .card--front .lockup__sub::before, .card--front .lockup__sub::after { width: 30px; }

  .card--back .lockup { left: 84px; top: 64px; width: 520px; }
  .card--back .lockup__tagline { font-size: 22px; text-align: left; padding-left: 40px; }
  .card--back .lockup__name { font-size: 74px; margin-top: 2px; }
  .card--back .lockup__sub { font-size: 27px; margin-top: 4px; gap: 12px; }
  .card--back .lockup__sub::before, .card--back .lockup__sub::after { width: 40px; }

  .contact {
    position: absolute; right: 362px; top: 242px;
    text-align: right;
    font-family: "Crimson Pro", serif; font-weight: 600;
  }
  .contact__phone { font-size: 40px; line-height: 1; text-align: center; }
  .contact__line { font-size: 16.5px; line-height: 1.15; }
  .contact__line:first-of-type { margin-top: 4px; }

  .divider {
    position: absolute; left: 338px; top: 241px; width: 2px; height: 84px; background: var(--gold);
  }
  .booking__icon { position: absolute; left: 358px; top: 245px; width: 66px; height: 66px; }
  .booking__text {
    position: absolute; left: 443px; top: 242px;
    font-family: "Crimson Pro", serif; font-weight: 600;
    font-size: 22px; line-height: 1.05; letter-spacing: 0.02em; text-transform: uppercase;
  }

  .social {
    position: absolute; left: 0; right: 0; top: 346px;
    display: flex; align-items: center; justify-content: center; gap: 10px;
    font-family: "Crimson Pro", serif; font-weight: 600; font-size: 18px;
  }
  .social__mark {
    width: 30px; height: 30px; border: 2.5px solid var(--gold); border-radius: 50%;
  }
</style>
</head>
<body>
<main class="stage">

  <section class="card card--front" aria-label="Business card front">
    <div class="card__photo" role="img" aria-label="Close-up beauty photograph of an eye with long lashes, soft blush tint"></div>
    <div class="lockup">
      <p class="lockup__tagline">Your Glow, Your Way.</p>
      <p class="lockup__name">VELVET FERN</p>
      <p class="lockup__sub">Beauty Bar by Marisol</p>
    </div>
  </section>

  <section class="card card--back" aria-label="Business card back">
    <div class="card__photo" role="img" aria-label="Soft-focus beauty portrait photograph, soft blush tint"></div>
    <div class="lockup">
      <p class="lockup__tagline">Your Glow, Your Way.</p>
      <p class="lockup__name">VELVET FERN</p>
      <p class="lockup__sub">Beauty Bar by Marisol</p>
    </div>

    <div class="contact">
      <p class="contact__phone">555.014.2287</p>
      <p class="contact__line">info@velvetfernbeautybar.com</p>
      <p class="contact__line">www.velvetfernbeautybar.com</p>
    </div>

    <div class="divider"></div>

    <svg class="booking__icon" viewBox="0 0 66 66" aria-hidden="true">
      <rect x="2" y="8" width="54" height="50" rx="6" fill="#1b1615"/>
      <rect x="13" y="2" width="6" height="13" rx="3" fill="#1b1615" stroke="#f3e1d9" stroke-width="2"/>
      <rect x="39" y="2" width="6" height="13" rx="3" fill="#1b1615" stroke="#f3e1d9" stroke-width="2"/>
      <rect x="2" y="20" width="54" height="3" fill="#b08d4c"/>
      <g fill="#f3e1d9">
        <rect x="9" y="28" width="9" height="8" rx="1.5"/><rect x="24" y="28" width="9" height="8" rx="1.5"/><rect x="39" y="28" width="9" height="8" rx="1.5"/>
        <rect x="9" y="42" width="9" height="8" rx="1.5"/><rect x="24" y="42" width="9" height="8" rx="1.5"/>
      </g>
      <circle cx="51" cy="52" r="13" fill="#b08d4c" stroke="#f3e1d9" stroke-width="3"/>
      <path d="M45 52 l4.5 4.5 L57 48" fill="none" stroke="#ffffff" stroke-width="3.2" stroke-linecap="round" stroke-linejoin="round"/>
    </svg>
    <p class="booking__text">Book your<br>appointment<br>today!</p>

    <div class="social">
      <span>Find us on:</span>
      <span class="social__mark" aria-hidden="true"></span>
      <span>@velvet_fern_beauty_bar</span>
    </div>
  </section>

</main>
</body>
</html>
```